Brisk needs a new design we have an updated logo and want a high qualitative high end feel

feel and aesthetic should be high qualitative like the packaging in a vexa or the qualatative weight/feel of an vexa design. modern, elegant bold.probably just the brisk logo on the backone vesion could be blue background white letter ... open to ideas
Target Market(s)
legal, insurance , medical, finance orb 700
Industry/Entity Type
Information Technology
Font styles to use
Serif

```html
<!DOCTYPE html>
<html lang="en">
<head>
<meta charset="utf-8">
<title>Brisk Business Card</title>
<link href="https://fonts.googleapis.com/css2?family=Open+Sans:wght@400;600;700&display=swap" rel="stylesheet">
<style>
  :root {
    --page: #9b9b9b;
    --card: #ffffff;
    --navy: #1b2a3d;
    --ink: #4a4a4a;
    --muted: #5a5a5a;
  }
  * { margin: 0; padding: 0; box-sizing: border-box; }
  html, body {
    width: 1133px; height: 1200px; overflow: hidden;
    background: var(--page);
    font-family: "Open Sans", Arial, sans-serif;
  }
  .canvas { position: relative; width: 1133px; height: 1200px; }
  .card {
    position: absolute; left: 219px; width: 696px; height: 397px;
    background: var(--card);
  }
  .card--front { top: 153px; }
  .card--back { top: 647px; height: 398px; }

  .holder { position: absolute; left: 51px; top: 54px; }
  .holder__name { font-size: 24px; font-weight: 700; color: var(--navy); line-height: 1; }
  .holder__title { font-size: 17px; color: var(--muted); margin-top: 6px; line-height: 1; }
  .holder__address { font-size: 17px; color: var(--ink); margin-top: 12px; line-height: 22px; }

  .contact { position: absolute; right: 52px; top: 50px; list-style: none; }
  .contact__item {
    display: flex; justify-content: flex-end; align-items: center;
    font-size: 17px; color: var(--ink); height: 22.5px;
  }
  .contact__icon { width: 16px; height: 16px; margin-left: 16px; fill: var(--navy); }

  .front-mark {
    position: absolute; left: 60px; bottom: 40px;
    font-size: 150px; font-weight: 600; color: var(--navy);
    line-height: 1; letter-spacing: -2px;
  }

  .lockup { position: absolute; left: 157px; top: 168px; display: flex; align-items: flex-end; }
  .lockup__name {
    font-size: 104px; font-weight: 400; color: var(--navy);
    line-height: 0.82; letter-spacing: 1px;
  }
  .lockup__tagline {
    margin-left: 20px; font-size: 15px; color: var(--muted);
    line-height: 22px; letter-spacing: 1px; text-transform: uppercase;
  }
  .back-web {
    position: absolute; left: 0; right: 0; top: 333px; text-align: center;
    font-size: 17px; color: var(--ink); letter-spacing: 0.55em;
  }
</style>
</head>
<body>
<main class="canvas">
  <section class="card card--front">
    <div class="holder">
      <p class="holder__name">Nora Ellison</p>
      <p class="holder__title">President</p>
      <p class="holder__address">412 Harbor Lane<br>Milford, CT 06460</p>
    </div>
    <ul class="contact">
      <li class="contact__item">(555) 0142-7730
        <svg class="contact__icon" viewBox="0 0 16 16" aria-hidden="true"><path d="M1 6c0-2 3-3 7-3s7 1 7 3v1h-3V5.5H4V7H1z"/><rect x="3" y="8" width="10" height="6" rx="1"/></svg>
      </li>
      <li class="contact__item">(555) 0186-2419
        <svg class="contact__icon" viewBox="0 0 16 16" aria-hidden="true"><path d="M4 1h8v14H4z M5.5 2.5v9h5v-9z M7.3 12.6h1.4v1.2H7.3z" fill-rule="evenodd"/></svg>
      </li>
      <li class="contact__item">(555) 0127-9054
        <svg class="contact__icon" viewBox="0 0 16 16" aria-hidden="true"><rect x="4" y="1" width="8" height="5"/><rect x="1" y="7" width="14" height="6" rx="1"/><rect x="4" y="12" width="8" height="3"/></svg>
      </li>
      <li class="contact__item">info@brisk.com
        <svg class="contact__icon" viewBox="0 0 16 16" aria-hidden="true"><path d="M1 3h14v1.5L8 9 1 4.5z M1 6l7 4.5L15 6v7H1z"/></svg>
      </li>
      <li class="contact__item">www.brisk.com
        <svg class="contact__icon" viewBox="0 0 16 16" aria-hidden="true"><circle cx="8" cy="8" r="7"/><path d="M5 4c2 1 1 3 3 3s1 3 0 4-2 1-2 2" stroke="#fff" stroke-width="1.4" fill="none"/></svg>
      </li>
    </ul>
    <p class="front-mark">brisk</p>
  </section>

  <section class="card card--back">
    <div class="lockup">
      <p class="lockup__name">brisk</p>
      <p class="lockup__tagline">Managed<br>Services<br>Group, Inc.</p>
    </div>
    <p class="back-web">www.brisk.com</p>
  </section>
</main>
</body>
</html>
```